New Zealand Export company needs business cards

We need new business cards to match our new logo for a company based in New Zealand who deal specifically with the Pacific Islands. We source, consolidate and ship products out of New Zealand to the Pacific Islands. Will attach our old ones and also new logo.
Would like the Islands we deal with and the areas of work we have access to, to be included on the business cards.

Contact Information for Business Card

T +64 9 571 3048
F +64 9 571 6285
12-18 Kowhai Lane, Drury, 2113
PO Box 814, Drury, Auckland 2247, New Zealand
www.falconfreight.example.nz
E sales@falconfreight.example.nz

Font styles to use
Sans Serif

Colors
85abd2
33a6d7
ffffff

Requirements
Must have
• A company of PWM

```html
<!DOCTYPE html>
<html lang="en">
<head>
<meta charset="utf-8">
<title>Falcon Freight Business Card</title>
<link rel="stylesheet" href="https://fonts.googleapis.com/css2?family=Lato:wght@400;700;900&display=swap">
<style>
  :root {
    --backdrop: #8a5a34;
    --kraft-light: #d2ae82;
    --kraft-mid: #c39c6c;
    --kraft-dark: #b08555;
    --ink: #17110c;
    --rule: #3a2a1c;
    --icon-glyph: #d2ae82;
  }
  * { margin: 0; padding: 0; box-sizing: border-box; }
  html, body {
    width: 1200px; height: 900px; overflow: hidden;
    background: var(--backdrop);
  }
  .stage { position: relative; width: 1200px; height: 900px; font-family: "Lato", sans-serif; color: var(--ink); }
  .card {
    position: absolute;
    width: 556px; height: 343px;
    background: linear-gradient(135deg, var(--kraft-light) 0%, var(--kraft-mid) 45%, var(--kraft-dark) 100%);
    box-shadow: 4px 5px 8px rgba(0,0,0,0.45);
  }
  .card--front { left: 330px; top: 90px; }
  .card--back { left: 330px; top: 470px; width: 558px; }

  .contact { position: absolute; inset: 0; text-align: center; }
  .contact__name { position: absolute; left: 0; right: 0; top: 56px; font-weight: 700; font-size: 19px; letter-spacing: 0.2px; }
  .contact__title { position: absolute; left: 0; right: 0; top: 78px; font-size: 16px; }
  .contact__icons { position: absolute; left: 180px; top: 106px; width: 200px; height: 22px; }
  .contact__lines { position: absolute; left: 0; right: 0; top: 136px; font-size: 16px; line-height: 20.3px; }
  .contact__divider { position: absolute; left: 180px; width: 200px; top: 226px; height: 1px; background: var(--rule); opacity: 0.6; }
  .contact__address { position: absolute; left: 0; right: 0; top: 237px; font-size: 16px; line-height: 20.3px; }

  .brand {
    position: absolute; left: 0; right: 0; top: 130px;
    text-align: center; font-weight: 900; font-size: 44px; letter-spacing: 2px;
    line-height: 52px;
  }
  .tagline { position: absolute; left: 0; right: 0; top: 280px; display: flex; justify-content: center; align-items: center; gap: 8px; }
  .tagline__rule { width: 75px; height: 1px; background: var(--ink); }
  .tagline__rule--right { width: 60px; }
  .tagline__text { font-weight: 700; font-size: 16px; letter-spacing: 0.3px; }
</style>
</head>
<body>
<main class="stage">
  <section class="card card--front" aria-label="Card front">
    <div class="contact">
      <h1 class="contact__name">MARCUS HALE</h1>
      <p class="contact__title">Managing Director</p>
      <svg class="contact__icons" viewBox="0 0 200 22" aria-hidden="true">
        <line x1="0" y1="11" x2="46" y2="11" stroke="#3a2a1c" stroke-width="1"/>
        <line x1="154" y1="11" x2="200" y2="11" stroke="#3a2a1c" stroke-width="1"/>
        <!-- phone -->
        <rect x="49" y="1" width="20" height="20" rx="3" fill="#17110c"/>
        <path d="M53 10 q6 -5 12 0 l-1 2 h-2 l-1-2 h-4 l-1 2 h-2 z M55 12 h8 v5 h-8 z" fill="#d2ae82"/>
        <!-- fax -->
        <rect x="73" y="1" width="20" height="20" rx="3" fill="#17110c"/>
        <path d="M78 5 h10 v4 h-10 z M76 10 h14 v6 h-14 z M79 14 h8 v4 h-8 z" fill="#d2ae82"/>
        <!-- mail -->
        <rect x="97" y="1" width="20" height="20" rx="3" fill="#17110c"/>
        <rect x="100" y="6" width="14" height="10" fill="none" stroke="#d2ae82" stroke-width="1.5"/>
        <path d="M100 6 l7 6 l7 -6" fill="none" stroke="#d2ae82" stroke-width="1.5"/>
        <!-- web -->
        <rect x="121" y="1" width="20" height="20" rx="3" fill="#17110c"/>
        <circle cx="131" cy="11" r="6" fill="#d2ae82"/>
        <path d="M128 8 q3 1 2 4 q2 1 3 3 M133 6 q1 2 3 2" fill="none" stroke="#17110c" stroke-width="1.3"/>
      </svg>
      <p class="contact__lines">
        +64 9 571 3048<br>
        +64 9 571 6285<br>
        sales@falconfreight.example.nz<br>
        www.falconfreight.example.nz
      </p>
      <div class="contact__divider"></div>
      <p class="contact__address">
        12-18 Kowhai Lane, Drury, 2113<br>
        PO Box 814, Drury, Auckland 2247<br>
        New Zealand
      </p>
    </div>
  </section>

  <section class="card card--back" aria-label="Card back">
    <p class="brand">FALCON FREIGHT</p>
    <div class="tagline">
      <span class="tagline__rule"></span>
      <span class="tagline__text">A COMPANY OF PWM</span>
      <span class="tagline__rule tagline__rule--right"></span>
    </div>
  </section>
</main>
</body>
</html>
```